Geschäftspapiere für Fliesenleger - Meisterbetrieb
Zielgruppe
Wir sind ein mittelständischer Fliesenleger - Meisterbetrieb und möchten unsere Geschäftspapiere erneuern. Unsere Kunden sind Privatkunden, Gewerbetreibende sowie Öffentliche Auftraggeber.
Aufgabenstellung
Unser Logo stellen wir Ihnen zur verfügung und soll unverändert bleiben.
Wir benötigen folgende Geschäftspapiere:
- Briefpapier DIN A4
- Notizblock Karriert DIN A4
- Visitenkarten 5,5 x 8,5 cm
- Kuvert DIN lang mit Fenster
- Kuvert DIN C4 mit Fenster
Bei der Farbe Rot handelt es sich um Verkehrsrot RAL 3020
Als Schriftart haben wir uns Helvetica Neue vorgestellt.
Wir bitten jedoch auch um Vorschläge anderer Moderner und gut lesbarer Schriftarten die für Print und Web bestens geeignet sind.
Wir wünschen uns ein Modernes und Schnörkelloses Design. Bei den Dateien habe ich Ihnen ein Stockphoto angehängt um Ihnen zu zeigen wie wir uns ein Cover oder eine Broschüre vorstellen können. Nur um Ihnen unsere Ideen / Vorstellungen näher zu bringen.

```html
<!DOCTYPE html>
<html lang="de">
<head>
<meta charset="utf-8">
<title>Fliesen-Kerber – Geschäftspapiere</title>
<link href="https://fonts.googleapis.com/css2?family=Arimo:wght@400;700&display=swap" rel="stylesheet">
<style>
:root{
  --red:#d4111b;
  --ink:#111111;
  --black:#000000;
  --paper:#ffffff;
  --window:#ececec;
  --grid:#e2e2e2;
}
*{margin:0;padding:0;box-sizing:border-box}
html,body{width:750px;height:1200px;overflow:hidden;background:#fff}
body{position:relative;font-family:"Arimo","Helvetica Neue",Arial,sans-serif;color:var(--ink)}
.sheet{position:absolute;width:535px;height:756px;background:var(--paper);box-shadow:0 1px 6px rgba(0,0,0,.2);overflow:hidden}
.letter-main{left:45px;top:41px}
.letter-mini{left:44px;top:900px;transform:scale(.323);transform-origin:0 0}
.notepad{left:283px;top:900px;transform:scale(.323);transform-origin:0 0}
.shape{position:absolute;left:0;top:0}
.wordmark{position:absolute;font-weight:700;color:var(--ink);white-space:nowrap;line-height:1;letter-spacing:.2px}
.sheet .wordmark{right:38px;top:76px;font-size:24px}
.sender{position:absolute;left:64px;top:132px;font-size:6.4px;white-space:nowrap}
.red{color:var(--red);font-weight:700}
.recipient{position:absolute;left:64px;top:153px;font-size:9.6px;line-height:11.9px}
.date{position:absolute;left:64px;top:240px;font-size:9.6px}
.fold{position:absolute;left:0;top:268px;width:8px;height:.6px;background:var(--red)}
.subject{position:absolute;left:64px;top:272px;font-size:9.6px;font-weight:700}
.body{position:absolute;left:64px;top:304px;font-size:9.4px;line-height:11.9px;white-space:nowrap}
.body p{margin-bottom:11.9px}
.footer{position:absolute;top:688px;font-size:7.2px;line-height:10px;white-space:nowrap}
.footer b{font-weight:700}
.f1{left:64px}.f2{left:149px}.f3{left:249px}.f4{left:391px}
.gap{height:10px}
.key{display:inline-block;width:10px;font-weight:700}
.grid{position:absolute;left:34px;top:90px;width:468px;height:614px;border:.8px solid var(--grid);
  background-image:linear-gradient(var(--grid) .8px,transparent .8px),linear-gradient(90deg,var(--grid) .8px,transparent .8px);
  background-size:13.4px 13.4px}
.pad-foot{position:absolute;top:716px;font-size:7.2px;line-height:10px;white-space:nowrap}
.p1{left:34px}.p2{left:130px}.p3{left:227px}.p4{left:332px}

.card{position:absolute;width:179px;height:116px;background:var(--paper);box-shadow:0 1px 5px rgba(0,0,0,.2);overflow:hidden}
.card-logo{left:527px;top:219px}
.card-contact{left:527px;top:353px}
.card-logo-mini{left:202px;top:954px;transform:scale(.363);transform-origin:0 0}
.card-contact-mini{left:202px;top:1002px;transform:scale(.363);transform-origin:0 0}
.card .wordmark{right:25px;top:62px;font-size:18px}
.holder{position:absolute;left:21px;top:34px}
.holder-name{font-size:11px;font-weight:700}
.holder-role{font-size:6px;margin-top:1px}
.card-addr{position:absolute;left:21px;top:66px;font-size:5.8px;line-height:7.4px;white-space:nowrap}
.card-tel{position:absolute;left:88px;top:66px;font-size:5.8px;line-height:7.4px;white-space:nowrap}
.card-tel .key{width:8px}

.envelope{position:absolute;background:var(--paper);box-shadow:0 1px 5px rgba(0,0,0,.2);overflow:hidden}
.env-c4{left:475px;top:879px;width:188px;height:265px}
.env-dl{left:521px;top:1017px;width:185px;height:92px}
.env-c4 .wordmark{left:44px;top:32px;font-size:7.4px}
.env-dl .wordmark{left:49px;top:24px;font-size:7.4px}
.window{position:absolute;background:var(--window);border-radius:3px;padding:5px 8px;font-size:2.6px;line-height:3.4px;white-space:nowrap}
.env-c4 .window{left:16px;top:48px;width:74px;height:45px}
.env-dl .window{left:17px;top:43px;width:75px;height:36px}
.window .win-sender{font-size:1.9px;margin-bottom:4px}
.env-web{position:absolute;left:16px;top:248px;font-size:2.4px;font-weight:700}
</style>
</head>
<body>

<!-- Letterhead, full size -->
<div class="sheet letter-main">
  <svg class="shape" width="535" height="756" viewBox="0 0 535 756">
    <polygon points="0,0 143,0 118,25 25,25 25,119 0,143" fill="var(--red)"/>
    <polygon points="535,711 535,756 490,756" fill="var(--black)"/>
  </svg>
  <div class="wordmark">Fliesen-Kerber</div>
  <div class="sender"><span class="red">KRBW Kerber GmbH</span> &nbsp;·&nbsp; Talweg 48 &nbsp;·&nbsp; 91790 Hohenfeld</div>
  <div class="recipient">Herr<br>Max Mustermann<br>Musterstraße 12<br>12345 Musterstadt</div>
  <div class="date">Hohenfeld, 5. Mai 2025</div>
  <div class="fold"></div>
  <div class="subject">Betreff: Briefbogen</div>
  <div class="body">
    <p>Sehr geehrter Herr Mustermann,</p>
    <p>falls Sie keine Probleme haben, diesen Blindtext schnell und zügig zu lesen, können<br>Sie sich glücklich schätzen. Der verantwortliche Art Director, der Ihnen höchstwahr-<br>scheinlich gerade diesen Entwurf präsentiert, versteht sein typografisches Handwerk<br>par excellence.</p>
    <p>Er hat diesen Copyblock weder gestaucht, gezerrt, noch in Versalien oder gar in<br>6 Punkt Rundgrotesk Outline gesetzt. Er hat ihn ganz einfach lesbar gemacht. Offenbar<br>sogar ziemlich gut, sonst hätten Sie wohl schon einige Zeilen zuvor die Leselust<br>verloren. Beachten Sie nur die Zeilenbreite, die er gewählt hat. Sie ist weder zu lang<br>noch zu kurz gewählt.</p>
    <p>Der dazugehörige Zeilenabstand ist ideal. Ihre Augen haben keinerlei Probleme,<br>vom Ende einer Zeile in die nächste zu gelangen. Um einen solchen Art Director kann<br>man Sie beneiden. Er nutzt den ihm gewährten gestalterischen Freiraum nicht, um<br>sich selbst darzustellen, sondern Sie. Er weiß, daß es Wichtiges über Ihr Unternehmen<br>oder Produkt zu sagen gibt.</p>
    <p>Und dem räumt er großzügig Platz ein. Dieser Mensch hat zweifelsohne nicht am<br>Mäschäßutzets Inschtitut of Gräfick Ahts studiert. Er besitzt keine Bücher von Arno<br>Lindqvist oder Petra Hollmann, und wenn doch, ordnet er sie im Regal unter Kunst ein.<br>Statt dessen pflegt er eine liebevoll innige Beziehung zu Büchern von Behrendt und<br>Ilse Korff. Er liest sie.</p>
    <p>Mit recht freundlichen Grüßen</p>
    <p>Jonas Kerber</p>
  </div>
  <div class="footer f1"><span class="red">KRBW Kerber GmbH</span><div class="gap"></div>Talweg 48<br>91790 Hohenfeld</div>
  <div class="footer f2"><span class="key">T</span> 09321 - 48 27 310<br><span class="key">F</span> 09321 - 48 27 322<br><span class="key">M</span> post@fliesen-kerber.de<br><span class="key">W</span> www.fliesen-kerber.de</div>
  <div class="footer f3"><b>Bankverbindung</b><br>Raiffeisenbank Altmühltal<br>IBAN: DE00 0000 0000 0000 0000 00<br>BIC: GENODEF1ALT</div>
  <div class="footer f4"><b>Geschäftsführer</b><br>Jonas Kerber<br>HRB 4412 Amtsgericht Ansbach<br>Ust. ID: DE298104557</div>
</div>

<!-- Business card, logo side -->
<div class="card card-logo">
  <svg class="shape" width="179" height="116" viewBox="0 0 179 116">
    <polygon points="0,0 95,0 83,12 12,12 12,83 0,95" fill="var(--red)"/>
    <polygon points="179,95 179,116 158,116" fill="var(--black)"/>
  </svg>
  <div class="wordmark">Fliesen-Kerber</div>
</div>

<!-- Business card, contact side -->
<div class="card card-contact">
  <svg class="shape" width="179" height="116" viewBox="0 0 179 116">
    <polygon points="84,0 179,0 179,96 166,83 166,12 96,12" fill="var(--red)"/>
    <polygon points="0,95 21,116 0,116" fill="var(--black)"/>
  </svg>
  <div class="holder"><div class="holder-name">Jonas Kerber</div><div class="holder-role">Geschäftsführer</div></div>
  <div class="card-addr"><span class="red">KRBW Kerber GmbH</span><br><br>Talweg 48<br>91790 Hohenfeld</div>
  <div class="card-tel"><span class="key">T</span> 09321 - 48 27 310<br><span class="key">F</span> 09321 - 48 27 322<br><span class="key">M</span> post@fliesen-kerber.de<br><span class="key">W</span> www.fliesen-kerber.de</div>
</div>

<!-- Letterhead, overview -->
<div class="sheet letter-mini">
  <svg class="shape" width="535" height="756" viewBox="0 0 535 756">
    <polygon points="0,0 143,0 118,25 25,25 25,119 0,143" fill="var(--red)"/>
    <polygon points="535,711 535,756 490,756" fill="var(--black)"/>
  </svg>
  <div class="wordmark">Fliesen-Kerber</div>
  <div class="sender"><span class="red">KRBW Kerber GmbH</span> &nbsp;·&nbsp; Talweg 48 &nbsp;·&nbsp; 91790 Hohenfeld</div>
  <div class="recipient">Herr<br>Max Mustermann<br>Musterstraße 12<br>12345 Musterstadt</div>
  <div class="date">Hohenfeld, 5. Mai 2025</div>
  <div class="fold"></div>
  <div class="subject">Betreff: Briefbogen</div>
  <div class="body">
    <p>Sehr geehrter Herr Mustermann,</p>
    <p>falls Sie keine Probleme haben, diesen Blindtext schnell und zügig zu lesen, können<br>Sie sich glücklich schätzen. Der verantwortliche Art Director, der Ihnen höchstwahr-<br>scheinlich gerade diesen Entwurf präsentiert, versteht sein typografisches Handwerk<br>par excellence.</p>
    <p>Er hat diesen Copyblock weder gestaucht, gezerrt, noch in Versalien oder gar in<br>6 Punkt Rundgrotesk Outline gesetzt. Er hat ihn ganz einfach lesbar gemacht. Offenbar<br>sogar ziemlich gut, sonst hätten Sie wohl schon einige Zeilen zuvor die Leselust<br>verloren. Beachten Sie nur die Zeilenbreite, die er gewählt hat. Sie ist weder zu lang<br>noch zu kurz gewählt.</p>
    <p>Der dazugehörige Zeilenabstand ist ideal. Ihre Augen haben keinerlei Probleme,<br>vom Ende einer Zeile in die nächste zu gelangen. Um einen solchen Art Director kann<br>man Sie beneiden. Er nutzt den ihm gewährten gestalterischen Freiraum nicht, um<br>sich selbst darzustellen, sondern Sie. Er weiß, daß es Wichtiges über Ihr Unternehmen<br>oder Produkt zu sagen gibt.</p>
    <p>Und dem räumt er großzügig Platz ein. Dieser Mensch hat zweifelsohne nicht am<br>Mäschäßutzets Inschtitut of Gräfick Ahts studiert. Er besitzt keine Bücher von Arno<br>Lindqvist oder Petra Hollmann, und wenn doch, ordnet er sie im Regal unter Kunst ein.<br>Statt dessen pflegt er eine liebevoll innige Beziehung zu Büchern von Behrendt und<br>Ilse Korff. Er liest sie.</p>
    <p>Mit recht freundlichen Grüßen</p>
    <p>Jonas Kerber</p>
  </div>
  <div class="footer f1"><span class="red">KRBW Kerber GmbH</span><div class="gap"></div>Talweg 48<br>91790 Hohenfeld</div>
  <div class="footer f2"><span class="key">T</span> 09321 - 48 27 310<br><span class="key">F</span> 09321 - 48 27 322<br><span class="key">M</span> post@fliesen-kerber.de<br><span class="key">W</span> www.fliesen-kerber.de</div>
  <div class="footer f3"><b>Bankverbindung</b><br>Raiffeisenbank Altmühltal<br>IBAN: DE00 0000 0000 0000 0000 00<br>BIC: GENODEF1ALT</div>
  <div class="footer f4"><b>Geschäftsführer</b><br>Jonas Kerber<br>HRB 4412 Amtsgericht Ansbach<br>Ust. ID: DE298104557</div>
</div>

<!-- Business cards, overview -->
<div class="card card-logo-mini">
  <svg class="shape" width="179" height="116" viewBox="0 0 179 116">
    <polygon points="0,0 95,0 83,12 12,12 12,83 0,95" fill="var(--red)"/>
    <polygon points="179,95 179,116 158,116" fill="var(--black)"/>
  </svg>
  <div class="wordmark">Fliesen-Kerber</div>
</div>
<div class="card card-contact-mini">
  <svg class="shape" width="179" height="116" viewBox="0 0 179 116">
    <polygon points="84,0 179,0 179,96 166,83 166,12 96,12" fill="var(--red)"/>
    <polygon points="0,95 21,116 0,116" fill="var(--black)"/>
  </svg>
  <div class="holder"><div class="holder-name">Jonas Kerber</div><div class="holder-role">Geschäftsführer</div></div>
  <div class="card-addr"><span class="red">KRBW Kerber GmbH</span><br><br>Talweg 48<br>91790 Hohenfeld</div>
  <div class="card-tel"><span class="key">T</span> 09321 - 48 27 310<br><span class="key">F</span> 09321 - 48 27 322<br><span class="key">M</span> post@fliesen-kerber.de<br><span class="key">W</span> www.fliesen-kerber.de</div>
</div>

<!-- Notepad, squared -->
<div class="sheet notepad">
  <svg class="shape" width="535" height="756" viewBox="0 0 535 756">
    <polygon points="0,0 143,0 118,25 25,25 25,119 0,143" fill="var(--red)"/>
    <polygon points="535,711 535,756 490,756" fill="var(--black)"/>
  </svg>
  <div class="wordmark">Fliesen-Kerber</div>
  <div class="grid"></div>
  <div class="pad-foot p1"><span class="red">KRBW Kerber GmbH</span></div>
  <div class="pad-foot p2">Talweg 48<br>91790 Hohenfeld</div>
  <div class="pad-foot p3"><span class="key">T</span> 09321 - 48 27 310<br><span class="key">F</span> 09321 - 48 27 322</div>
  <div class="pad-foot p4"><span class="key">M</span> post@fliesen-kerber.de<br><span class="key">W</span> www.fliesen-kerber.de</div>
</div>

<!-- Envelope C4 with window -->
<div class="envelope env-c4">
  <svg class="shape" width="188" height="265" viewBox="0 0 188 265">
    <polygon points="0,0 46,0 38,8 8,8 8,38 0,46" fill="var(--red)"/>
    <polygon points="188,251 188,265 174,265" fill="var(--black)"/>
  </svg>
  <div class="wordmark">Fliesen-Kerber</div>
  <div class="window">
    <div class="win-sender"><span class="red">KRBW Kerber GmbH</span> · Talweg 48 · 91790 Hohenfeld</div>
    Herr<br>Max Mustermann<br>Musterstraße 12<br>12345 Musterstadt
  </div>
  <div class="env-web">www.fliesen-kerber.de</div>
</div>

<!-- Envelope DL with window -->
<div class="envelope env-dl">
  <svg class="shape" width="185" height="92" viewBox="0 0 185 92">
    <polygon points="0,0 36,0 30,6 6,6 6,30 0,36" fill="var(--red)"/>
    <polygon points="185,83 185,92 176,92" fill="var(--black)"/>
  </svg>
  <div class="wordmark">Fliesen-Kerber</div>
  <div class="window">
    <div class="win-sender"><span class="red">KRBW Kerber GmbH</span> · Talweg 48 · 91790 Hohenfeld</div>
    Herr<br>Max Mustermann<br>Musterstraße 12<br>12345 Musterstadt
  </div>
</div>

</body>
</html>
```